Velmora - 3D medical animations and high end visual content

Our company creates high end visual content and animations for medical global companies.
Our website - www.velmora-studio.example
We would like to have an amazing business card for our CEO that he can use in the following exhebitions he is going to attend.
It is very important that the design will be memorable and diffrent. It has to reflect our brand design (you can have it from our website)
We would like to transmit innovation, prestige, luxury, aesthetics.
The card has to be Double Sided

Target Market(s)

Marketing managers in medical global companys

Industry/Entity Type

It Company

Contact Information for Business Card

Requirements
Nice to have
• It is very important that the design will be memorable and diffrent. It has to reflect our brand design (you can have it from our website)

```html
<!DOCTYPE html>
<html lang="en">
<head>
<meta charset="utf-8">
<title>Velmora – Business Card</title>
<link rel="stylesheet" href="https://fonts.googleapis.com/css2?family=Source+Sans+3:wght@400;600;700&display=swap">
<style>
  :root {
    --stage: #000000;
    --card-dark: #1e1d1f;
    --brand-teal: #169aae;
    --teal-text: #2fa8bd;
    --white: #ffffff;
  }
  html, body {
    margin: 0;
    padding: 0;
    width: 1200px;
    height: 900px;
    overflow: hidden;
    background: var(--stage);
    font-family: "Source Sans 3", "Helvetica Neue", Arial, sans-serif;
  }
  .canvas {
    position: relative;
    width: 1200px;
    height: 900px;
  }
  .card {
    position: absolute;
    top: 275px;
    width: 477px;
    height: 294px;
    overflow: hidden;
  }
  .card-front {
    left: 116px;
    background: var(--card-dark);
    border-radius: 0 46px 0 46px;
  }
  .card-back {
    left: 622px;
    background: var(--brand-teal);
    border-radius: 46px 0 46px 0;
  }
  .brand-name {
    position: absolute;
    color: var(--white);
    font-weight: 600;
    letter-spacing: 0.06em;
    text-transform: uppercase;
    line-height: 1;
    white-space: nowrap;
  }
  .card-front .brand-name {
    right: 26px;
    top: 62px;
    font-size: 38px;
  }
  .card-back .brand-name {
    left: 0;
    right: 0;
    top: 118px;
    text-align: center;
    font-size: 42px;
  }
  .pattern-field {
    position: absolute;
    inset: 0;
    background: linear-gradient(180deg, #1a9db1 0%, #1596aa 100%);
  }
  .holder {
    position: absolute;
    left: 24px;
    top: 157px;
    right: 0;
  }
  .holder-name {
    display: flex;
    align-items: center;
    gap: 8px;
    color: var(--teal-text);
    font-weight: 700;
    font-size: 18px;
    letter-spacing: 0.01em;
    line-height: 1;
  }
  .holder-name::after {
    content: "";
    flex: 1;
    height: 1.5px;
    background: var(--white);
  }
  .holder-title {
    margin-top: 5px;
    color: var(--white);
    font-size: 13.5px;
    letter-spacing: 0.01em;
  }
  .contact-list {
    position: absolute;
    right: 24px;
    top: 200px;
    margin: 0;
    padding: 0;
    list-style: none;
    text-align: right;
  }
  .contact-list li {
    display: flex;
    justify-content: flex-end;
    align-items: center;
    gap: 5px;
    height: 17.5px;
    color: var(--white);
    font-size: 13.5px;
  }
  .contact-icon {
    width: 10px;
    height: 10px;
    flex: none;
  }
</style>
</head>
<body>
<main class="canvas">
  <section class="card card-front" aria-label="Business card front">
    <div class="brand-name">Velmora</div>
    <div class="holder">
      <div class="holder-name">NOAM KELLER</div>
      <div class="holder-title">FOUNDER &amp; CEO</div>
    </div>
    <ul class="contact-list">
      <li>+972-50-0001234
        <svg class="contact-icon" viewBox="0 0 10 10"><rect x="2.5" y="0.5" width="5" height="9" rx="1" fill="none" stroke="#2fa8bd" stroke-width="1.2"/><circle cx="5" cy="8" r="0.6" fill="#2fa8bd"/></svg>
      </li>
      <li>+972-70-0005678
        <svg class="contact-icon" viewBox="0 0 10 10"><path d="M1 4 Q5 0.5 9 4 L8 5.5 L6.5 4.5 L3.5 4.5 L2 5.5 Z" fill="#2fa8bd"/><rect x="2" y="5.5" width="6" height="3.5" rx="0.6" fill="#2fa8bd"/></svg>
      </li>
      <li>noam@velmora-studio.example
        <svg class="contact-icon" viewBox="0 0 10 10"><rect x="0.5" y="2" width="9" height="6.5" fill="#2fa8bd"/><path d="M0.5 2 L5 5.8 L9.5 2" fill="none" stroke="#1e1d1f" stroke-width="0.9"/></svg>
      </li>
      <li>www.velmora-studio.example
        <svg class="contact-icon" viewBox="0 0 10 10"><circle cx="5" cy="5" r="4.5" fill="#2fa8bd"/><path d="M3 3 Q5 4 4 6 Q6 7 7 5" fill="none" stroke="#1e1d1f" stroke-width="0.9"/></svg>
      </li>
    </ul>
  </section>

  <section class="card card-back" aria-label="Business card back">
    <div class="pattern-field" role="img" aria-label="Faint repeated brand name pattern across the card background"></div>
    <div class="brand-name">Velmora</div>
  </section>
</main>
</body>
</html>
```